Business card for a "family office" company

Please provide professional looking business card designs, incorporating the attached logo and below details. Harrowmere Holdings Pty Ltd is a family office / financial investment company. We are looking for a modern, professional and contemporary card design.

Industry/Entity Type

Finance

Contact Information for Business Card

Name: Dean Mollick
Title: Director
Company: Harrowmere Holdings Pty Ltd
Email: harrowdean@quillnet.example
Mobile: 0462 735 418
Address: 4/312 Barnaby Parade, Cottesloe WA 6011, Australia

Requirements
Must have
• All details above and the logo. logo only on back side. incorporate colours of logo
Nice to have
• up to you
Should not have
• ?

```html
<!DOCTYPE html>
<html lang="en">
<head>
<meta charset="utf-8">
<title>Harrowmere Holdings – Business Card</title>
<link rel="stylesheet" href="https://fonts.googleapis.com/css2?family=Open+Sans:wght@400;600;700&display=swap">
<style>
  :root {
    --navy-deep: #25244f;
    --navy: #34336a;
    --navy-mid: #45437a;
    --navy-soft: #575389;
    --band-light: #5d5ca6;
    --ink: #2b2a5e;
    --paper: #ffffff;
    --backdrop: #ececee;
    --text-light: #ffffff;
    --text-muted: #c9c8e0;
  }
  * { margin: 0; padding: 0; box-sizing: border-box; }
  html, body {
    width: 1200px;
    height: 533px;
    overflow: hidden;
    background: var(--backdrop);
    font-family: "Open Sans", sans-serif;
  }
  .stage {
    position: relative;
    width: 1200px;
    height: 533px;
  }
  .card {
    position: absolute;
    top: 84px;
    width: 545px;
    height: 309px;
    background: var(--paper);
    overflow: hidden;
    box-shadow: 0 2px 10px rgba(0, 0, 0, 0.12);
  }
  .card--front { left: 60px; }
  .card--back { left: 620px; width: 540px; }
  .card__waves {
    position: absolute;
    inset: 0;
    width: 100%;
    height: 100%;
  }
  .holder {
    position: absolute;
    left: 36px;
    top: 26px;
    color: var(--text-light);
  }
  .holder__name {
    font-size: 10px;
    font-weight: 700;
    letter-spacing: 0.04em;
    text-transform: uppercase;
  }
  .holder__title {
    margin-top: 4px;
    font-size: 7.5px;
    color: var(--text-muted);
    letter-spacing: 0.05em;
    text-transform: uppercase;
  }
  .company-line {
    position: absolute;
    right: 20px;
    top: 26px;
    font-size: 8px;
    font-weight: 700;
    letter-spacing: 0.04em;
    color: var(--text-light);
    text-transform: uppercase;
  }
  .contact {
    position: absolute;
    left: 36px;
    top: 206px;
    list-style: none;
    font-size: 7.5px;
    color: var(--ink);
    text-transform: uppercase;
    letter-spacing: 0.04em;
  }
  .contact__row {
    display: flex;
    height: 19.5px;
    align-items: center;
  }
  .contact__label {
    width: 43px;
    font-weight: 600;
  }
  .wordmark {
    position: absolute;
    color: var(--ink);
    font-weight: 600;
    text-align: center;
    text-transform: uppercase;
    line-height: 1.15;
  }
  .wordmark--small {
    right: 20px;
    top: 222px;
    font-size: 11px;
    letter-spacing: 0.06em;
  }
  .wordmark--large {
    left: 0;
    right: 0;
    top: 150px;
    font-size: 30px;
    letter-spacing: 0.08em;
  }
</style>
</head>
<body>
<main class="stage">

  <section class="card card--front" aria-label="Business card front">
    <svg class="card__waves" viewBox="0 0 545 309" preserveAspectRatio="none" aria-hidden="true">
      <path fill="var(--navy-soft)" d="M0 0H545V188C470 176 410 160 330 168C240 177 150 196 70 186C40 182 18 178 0 176Z"/>
      <path fill="var(--navy-mid)" d="M0 0H545V172C470 158 400 146 320 156C230 167 140 182 60 170C35 166 16 160 0 156Z"/>
      <path fill="var(--navy)" d="M0 0H545V150C470 132 400 118 310 124C220 130 130 150 50 140C28 137 12 132 0 128Z"/>
      <path fill="var(--navy-deep)" d="M0 0H545V95C470 108 380 116 300 110C200 102 110 80 0 92Z" opacity="0.35"/>
    </svg>

    <div class="holder">
      <p class="holder__name">Dean Mollick</p>
      <p class="holder__title">Director</p>
    </div>
    <p class="company-line">Harrowmere Holdings Pty Ltd</p>

    <ul class="contact">
      <li class="contact__row"><span class="contact__label">Email:</span><span>harrowdean@quillnet.example</span></li>
      <li class="contact__row"><span class="contact__label">Mobile:</span><span>0462 735 418</span></li>
      <li class="contact__row"><span class="contact__label">Address:</span><span>4/312 Barnaby Parade, Cottesloe WA 6011, Australia</span></li>
    </ul>

    <p class="wordmark wordmark--small">Harrowmere<br>Holdings</p>
  </section>

  <section class="card card--back" aria-label="Business card back">
    <svg class="card__waves" viewBox="0 0 540 309" preserveAspectRatio="none" aria-hidden="true">
      <path fill="var(--band-light)" d="M0 0H540V52C480 50 420 42 340 48C250 55 170 70 90 66C50 64 20 58 0 58Z"/>
      <path fill="var(--navy-deep)" d="M0 0H540V40C470 34 410 28 330 34C240 41 160 56 80 50C45 47 18 42 0 42Z"/>
    </svg>

    <p class="wordmark wordmark--large">Harrowmere<br>Holdings</p>
  </section>

</main>
</body>
</html>
```